Tour operator needs simple coded WordPress site (updated extra payment for coding and guaranteed)

[update 9/7/2015]
If you design a new logo and it gets accepted, even if we use another template with your logo you will get $50
[update 8/7/2015]
Update on questions about dual-language
For dual languages we are happy to set up a second site with the same designs in a second language.
For the design aspect just allow the user to switch between languages with an icon.
For the coding, a replica of the site on a second server will do (to save messing around with multiple language plugins) - we will populate it with Chinese text
[original post]
Simple coded WordPress site for tours
You can choose to design only or design and code ($340 design, $150 bonus for coding)
Open design brief - use your creativity
Will be in 2 languages (English and Chinese) but design needs only to be in one language
Winning design will be chosen only from home page, but the winner must make a second standard template page when chosen at no extra cost.
Must be responsive design
We only need homepage and standard template page design and coding, we will populate the pages
You can use design ideas from our pamphlet if you like - attached
Only a sample logo and colors on website and pamphlet - feel free to change as the current ones seem restrictive
Current website framework only to give an idea of the number of pages and basic menu structure (no need to use existing navigation style or any style at all for that matter, open brief)
http://brightwattlejourneys.com.au/
Target Market(s)
Chinese parents of kids 10-14 (the kids will take the tour)
Industry/Entity Type
Tour
Number of Pages Required
2 page
Look and feel
Each slider illustrates characteristics of the customer's brand and the style your logo design should communicate.

```html
<!DOCTYPE html>
<html lang="en">
<head>
<meta charset="utf-8">
<title>Bright Wattle Journeys</title>
<link href="https://fonts.googleapis.com/css2?family=Open+Sans:wght@400;600;700&family=Varela+Round&family=Arvo:wght@400;700&display=swap" rel="stylesheet">
<style>
:root{
  --green:#24a97b;
  --green-dark:#188a61;
  --green-deep:#127050;
  --ink:#3a3a3a;
  --muted:#777;
  --paper:#ffffff;
  --card:#f1f1f1;
  --line:#dcdcdc;
  --hero-a:#3e4a55;
  --hero-b:#8a7a64;
}
*{margin:0;padding:0;box-sizing:border-box}
html,body{width:1200px;height:2804px;overflow:hidden}
body{font-family:'Open Sans',sans-serif;color:var(--ink);background:var(--paper);position:relative}
.heading{font-family:'Varela Round',sans-serif;font-weight:400}

.hero{position:absolute;top:0;left:0;width:1200px;height:560px;background:linear-gradient(135deg,#2f3a44 0%,var(--hero-a) 35%,var(--hero-b) 70%,#5a5048 100%)}
.hero-shade{position:absolute;inset:0;background:rgba(0,0,0,.28)}
.brand{position:absolute;top:24px;left:0;width:1200px;text-align:center;color:#fff;font-size:22px;font-weight:700;letter-spacing:1px}
.brand .dot{display:inline-block;width:14px;height:14px;background:var(--green);margin-right:10px;vertical-align:middle}
.lang{position:absolute;top:12px;right:16px;color:#fff;font-size:11px;background:rgba(0,0,0,.35);padding:3px 8px}
.values{position:absolute;top:340px;left:0;width:1200px;display:flex;justify-content:center;align-items:flex-end;color:#fff;gap:0}
.value{text-align:center;font-weight:700;font-size:21px;letter-spacing:1px;padding:0 30px}
.value svg{display:block;margin:0 auto 12px}
.sep{font-size:21px;font-weight:700;color:#fff;padding-bottom:2px}

.nav{position:absolute;top:560px;left:0;width:1200px;height:48px;background:var(--green);display:flex;justify-content:center}
.nav a{color:#fff;text-decoration:none;font-size:12px;font-weight:700;width:108px;line-height:48px;text-align:center}
.nav a.active{background:var(--green-deep)}

.welcome{position:absolute;top:608px;left:0;width:1200px;text-align:center}
.welcome h1{font-size:34px;color:#555;margin-top:46px}
.welcome p{width:900px;margin:22px auto 0;font-size:13px;line-height:26px;color:var(--muted)}

.about{position:absolute;top:900px;left:0;width:1200px;height:260px;background:var(--green);text-align:center;color:#fff}
.about h2{font-size:32px;margin-top:30px}
.about p{width:900px;margin:18px auto 0;font-size:12.5px;line-height:24px;opacity:.95}

.slider{position:absolute;top:1272px;left:0;width:1200px;height:152px;background:linear-gradient(90deg,#2a2f33,#5b5e61 50%,#2d3135)}
.slider-title{position:absolute;top:56px;left:0;width:1200px;text-align:center;color:#fff;font-size:34px}
.arrow{position:absolute;top:58px}
.tabs{position:absolute;top:1424px;left:0;width:1200px;height:96px;background:var(--green);display:flex;justify-content:center}
.tab{width:180px;text-align:center;color:#fff;font-size:13px;font-weight:600;padding-top:18px}
.tab.active{background:var(--green-deep)}
.tab svg{display:block;margin:0 auto 10px}

.tours{position:absolute;top:1580px;left:0;width:1200px;text-align:center}
.tours h2{font-size:40px;color:#444}
.tours .lede{width:860px;margin:18px auto 0;font-size:12.5px;line-height:22px;color:var(--muted)}
.cards{position:absolute;top:1780px;left:64px;width:1072px;display:flex;gap:12px}
.card{flex:1;height:320px;background:var(--card);padding:28px 24px;text-align:left}
.card h3{font-size:22px;font-weight:600;color:#333}
.card .dates{font-size:13px;font-weight:600;margin-top:26px}
.card .places{font-size:13px;font-weight:700;margin-top:20px}
.card .blurb{font-size:11.5px;line-height:19px;color:var(--muted);margin-top:16px}
.btn{display:inline-block;margin-top:22px;font-size:11.5px;padding:7px 14px;background:#ddd;color:#333}
.btn.primary{background:var(--green);color:#fff}
.view-all{position:absolute;top:2116px;right:64px;font-size:12px;color:#555}

.newsletter{position:absolute;top:2196px;left:0;width:1200px;text-align:center}
.newsletter h2{font-family:'Arvo',serif;font-weight:400;font-size:30px;color:var(--green)}
.signup{margin:28px auto 0;display:flex;justify-content:center}
.signup .field{width:210px;height:38px;border:1px solid var(--line);font-size:11px;color:#999;line-height:36px;text-align:left;padding-left:12px}
.signup .go{width:130px;height:38px;background:var(--green);color:#fff;font-size:12px;font-weight:700;line-height:38px}

.bottom{position:absolute;top:2380px;left:64px;width:1072px;height:330px;display:flex}
.col{flex:1;position:relative}
.col h3{font-size:22px;font-weight:600;color:#333}
.divider{width:1px;background:var(--line);margin:0 30px}
.quote{margin-top:26px;width:420px;border:1px solid var(--line);border-radius:6px;padding:18px 20px 70px;font-size:11.5px;line-height:19px;color:var(--muted);position:relative}
.person{position:absolute;left:24px;bottom:-30px;display:flex;align-items:center;gap:14px}
.avatar{width:70px;height:70px;border-radius:50%;background:linear-gradient(135deg,#d9b99a,#8a6a50);border:3px solid #fff}
.person b{font-size:18px;color:#333;margin-top:18px}
.gallery{margin-top:26px;display:grid;grid-template-columns:repeat(4,100px);gap:8px;justify-content:center}
.gallery div{height:80px}
.pager{position:absolute;bottom:0}
.col.left .pager{left:220px}
.col.right .pager{right:80px}
.col.right h3{text-align:center}

.footer{position:absolute;top:2752px;left:0;width:1200px;height:52px;background:var(--green);color:#fff;font-size:11px;font-weight:700;text-align:center;line-height:52px}
.footer .up{position:absolute;right:70px;top:18px}
</style>
</head>
<body>

<header class="hero" role="img" aria-label="Photo of smiling students studying together outdoors">
  <div class="hero-shade"></div>
  <div class="brand"><span class="dot"></span>Bright Wattle Journeys</div>
  <div class="lang">Select Language</div>
  <div class="values">
    <div class="value"><svg width="30" height="30" viewBox="0 0 30 30"><path d="M4 8 L15 4 L26 8 L26 24 L15 28 L4 24Z" fill="none" stroke="#fff" stroke-width="2.5"/><path d="M15 4 V28" stroke="#fff" stroke-width="2"/></svg>EDUCATIONAL</div>
    <div class="sep">|</div>
    <div class="value"><svg width="30" height="30" viewBox="0 0 30 30"><path d="M15 3 L26 7 V15 C26 21 21 26 15 28 C9 26 4 21 4 15 V7Z" fill="#fff"/></svg>SAFE</div>
    <div class="sep">|</div>
    <div class="value"><svg width="30" height="30" viewBox="0 0 30 30"><path d="M15 2 L17 12 L28 17 L28 19 L17 17 L16 25 L19 27 L19 28 L15 27 L11 28 L11 27 L14 25 L13 17 L2 19 L2 17 L13 12Z" fill="#fff"/></svg>CULTURALLY ENLIGHTENING</div>
    <div class="sep">|</div>
    <div class="value"><svg width="30" height="30" viewBox="0 0 30 30"><circle cx="15" cy="15" r="12" fill="none" stroke="#fff" stroke-width="2.5"/><circle cx="11" cy="12" r="1.8" fill="#fff"/><circle cx="19" cy="12" r="1.8" fill="#fff"/><path d="M9 18 Q15 24 21 18" fill="none" stroke="#fff" stroke-width="2.2"/></svg>FUN</div>
  </div>
</header>

<nav class="nav">
  <a class="active">HOME</a><a>ABOUT US</a><a>TOURS</a><a>CONTACT</a>
</nav>

<section class="welcome">
  <h1 class="heading">Welcome!</h1>
  <p>At Bright Wattle Journeys we are passionate about educational travel and providing opportunities for students to learn more about Australia and gain a deeper understanding of the culture. The out of classroom experience gained on our trips is invaluable. Taking the Bright Wattle Journeys tour is easy because our team of dedicated experts assists every step of the way – from meticulously planning the curriculum to planning every detail of your trip to accompanying you on tour.</p>
</section>

<section class="about">
  <h2 class="heading">About Us!</h2>
  <p>We inspect every hotel, visit every attraction, evaluate every teacher and sample every restaurant. Wherever you go on tour, we've been there, and we always listen to our travellers. We are known for our exceptional standards. We have an extensive team of specialists to help you with all your travel needs. We have staff that have travelled around Australia and can use their first hand knowledge to help make your tour educational, enjoyable and hassle free.</p>
</section>

<section class="slider" role="img" aria-label="Photo of students working on tablets in a classroom">
  <svg class="arrow" style="left:96px" width="20" height="36" viewBox="0 0 20 36"><path d="M16 4 L4 18 L16 32" fill="none" stroke="#fff" stroke-width="3"/></svg>
  <div class="slider-title heading">We craft practical solutions</div>
  <svg class="arrow" style="right:96px" width="20" height="36" viewBox="0 0 20 36"><path d="M4 4 L16 18 L4 32" fill="none" stroke="#fff" stroke-width="3"/></svg>
</section>

<div class="tabs">
  <div class="tab active"><svg width="26" height="26" viewBox="0 0 26 26"><path d="M3 7 L13 3 L23 7 V21 L13 24 L3 21Z" fill="#fff"/></svg>Cultural education</div>
  <div class="tab"><svg width="26" height="26" viewBox="0 0 26 26"><path d="M13 2 L15 10 L24 14 V16 L15 14 L14 21 L17 23 V24 L13 23 L9 24 V23 L12 21 L11 14 L2 16 V14 L11 10Z" fill="#fff"/></svg>Cultural activities</div>
  <div class="tab"><svg width="26" height="26" viewBox="0 0 26 26"><circle cx="13" cy="13" r="10" fill="none" stroke="#fff" stroke-width="2.5"/><path d="M13 3 A10 10 0 0 1 13 23Z" fill="#fff"/></svg>Cultural Tours</div>
</div>

<section class="tours">
  <h2 class="heading">Special Tours</h2>
  <p class="lede">Lorem ipsum dolor sit amet, consectetur adipiscing elit, sed do eiusmod tempor incididunt ut labore et dolore magna aliqua. Ut enim ad minim veniam, quis nostrud lorem ipsum dolor sit amet, consectetur adipiscing elit.</p>
</section>

<div class="cards">
  <article class="card">
    <h3>July</h3>
    <div class="dates">July 4th – July 17th 2015</div>
    <div class="places">13 places available</div>
    <p class="blurb">Lorem ipsum dolor sit amet, consectetur adipiscing elit, sed do eiusmod</p>
    <span class="btn primary">Join Now</span>
  </article>
  <article class="card">
    <h3>July</h3>
    <div class="dates">July 18th – July 31st 2015</div>
    <div class="places">13 places available</div>
    <p class="blurb">Lorem ipsum dolor sit amet, consectetur adipiscing elit, sed do eiusmod</p>
    <span class="btn">Join Now</span>
  </article>
  <article class="card">
    <h3>August</h3>
    <div class="dates">August 1st to August 14th 2015</div>
    <div class="places">13 places available</div>
    <p class="blurb">Lorem ipsum dolor sit amet, consectetur adipiscing elit, sed do eiusmod</p>
    <span class="btn">Join Now</span>
  </article>
</div>
<div class="view-all">View All</div>

<section class="newsletter">
  <h2>Sign up to our newsletter to receive our latest news by email:</h2>
  <div class="signup"><div class="field">ENTER YOUR EMAIL HERE</div><div class="go">SUBSCRIBE</div></div>
</section>

<section class="bottom">
  <div class="col left">
    <h3>Testimonial</h3>
    <div class="quote">"Lorem ipsum dolor sit amet, consectetur adipiscing elit. Sed do eiusmod tempor incididunt ut labore et dolore magna aliqua. Ut enim ad minim veniam, quis nostrud exercitation."
      <div class="person"><div class="avatar" role="img" aria-label="Portrait of the reviewer"></div><b>Clara Hewitt</b></div>
    </div>
    <svg class="pager" width="60" height="24" viewBox="0 0 60 24"><path d="M14 4 L6 12 L14 20" fill="none" stroke="var(--green)" stroke-width="2.5"/><path d="M46 4 L54 12 L46 20" fill="none" stroke="var(--green)" stroke-width="2.5"/></svg>
  </div>
  <div class="divider"></div>
  <div class="col right">
    <h3>Latest gallery</h3>
    <div class="gallery">
      <div role="img" aria-label="Gallery photo of a coastline" style="background:linear-gradient(#8fbfe0,#c9a16b)"></div>
      <div role="img" aria-label="Gallery photo of a harbour" style="background:linear-gradient(#6fa8d6,#3c6e90)"></div>
      <div role="img" aria-label="Gallery photo of red flowers" style="background:linear-gradient(#c0392b,#6b8e3d)"></div>
      <div role="img" aria-label="Gallery photo of city buildings" style="background:linear-gradient(#9aa6b0,#5b6670)"></div>
      <div role="img" aria-label="Gallery photo of a beach" style="background:linear-gradient(#9fd0e6,#e0cfa0)"></div>
      <div role="img" aria-label="Gallery photo of a landmark" style="background:linear-gradient(#7a8fa0,#b89a78)"></div>
      <div role="img" aria-label="Gallery photo of a sunset" style="background:linear-gradient(#e6a04a,#7a4a3a)"></div>
      <div role="img" aria-label="Gallery photo of rocky hills" style="background:linear-gradient(#a3b6c4,#8a6d4e)"></div>
    </div>
    <svg class="pager" width="60" height="24" viewBox="0 0 60 24"><path d="M14 4 L6 12 L14 20" fill="none" stroke="var(--green)" stroke-width="2.5"/><path d="M46 4 L54 12 L46 20" fill="none" stroke="var(--green)" stroke-width="2.5"/></svg>
  </div>
</section>

<footer class="footer">Copyright © 2015 Bright Wattle Journeys
  <svg class="up" width="26" height="16" viewBox="0 0 26 16"><path d="M3 13 L13 3 L23 13" fill="none" stroke="#fff" stroke-width="2.5"/></svg>
</footer>

</body>
</html>
```